Flyer Design for Private Tuition

Brightpath Tutoring (www.BrightpathTutoring.co.uk) is an after school/ weekend tutoring service for students aged 4-18 years olds. Please look at our website for further information about our features and benefits. However something I think may be good to add is: Money back guarantee, Free trial, Free assessment. I would like it to include a £25 voucher symbol.

I have uploaded the following:
- Helmsworth Bank logo for the colour I want (Light Blue with white)

Please also look at our website: www.BrightpathTutoring.com

Please contact me for any further info. Good luck!
Updates

Project Deadline Extended Reason: We have decided to extend the deadline as we feel we need more time to get to where we need to be with the leafet. Added Saturday, January 16, 2016

Target Market(s)

Parents of children aged 4-18 years old.

Industry/Entity Type

Education

Colors
85cae6
ffffff

Requirements
Must have
• My logo should be LIGHT BLUE logo colours of like these companies:
• http://www.helmsworth.co.uk
• https://www.morvantek.com
• Background should be white.
• Must be a clean, fresh look and feel.
Nice to have
• A nice Brightpath Tutoring logo
• An image of an A* ..... or maybe an A* graded on a piece of work.... or maybe some kind of award/ achievement or something like that. This would signify the feeling of success to the target market (parents).
Should not have
• Due to religious reasons I do not want any pictures of human/animal faces. Blurred out faces or parts of bodies are ok, (Perhaps you could use images of an A* Grade? Success/ Achievement? Graduation hat? Stationary?)
• Please do not include the PLD Education logo (this is the parent company but it will be confusing to include it).

```html
<!DOCTYPE html>
<html lang="en">
<head>
<meta charset="utf-8">
<title>Brightpath Tutoring Flyer</title>
<link rel="stylesheet" href="https://fonts.googleapis.com/css2?family=Quicksand:wght@500;600;700&family=Questrial&display=swap">
<style>
:root{
  --sky:#4ab3e2;
  --sky-soft:#d6ecf8;
  --title:#1e9fdc;
  --navy:#1f3553;
  --ink:#2e4c6c;
  --orange:#f58a1f;
  --panel:#dcdde0;
  --white:#ffffff;
}
*{margin:0;padding:0;box-sizing:border-box}
html,body{width:846px;height:1200px;overflow:hidden}
body{background:var(--white);font-family:"Quicksand",sans-serif;color:var(--navy)}
.flyer{position:relative;width:846px;height:1200px;overflow:hidden;
  background:linear-gradient(160deg,#c9e6f6 0%,#eef7fc 35%,#ffffff 60%,#eaf4fb 100%)}
.abs{position:absolute}
.brand{left:30px;top:40px;display:flex;align-items:center;gap:14px}
.brand-dot{width:84px;height:84px;border-radius:50%;background:var(--sky)}
.brand-name{font-family:"Quicksand",sans-serif;font-weight:700;font-size:48px;color:var(--sky);letter-spacing:-.5px}
.tagline{left:280px;top:112px;z-index:2;padding:2px 10px;background:var(--white);font-weight:700;font-size:20px;color:var(--orange)}
.photo{left:462px;top:140px;width:350px;height:455px;z-index:1;
  background:linear-gradient(180deg,#f2f2f2 0%,#e9e9ea 40%,#f4f4f6 70%,#e6ebf0 100%);border-radius:4px}
.intro{left:36px;top:168px;width:418px;font-weight:700;font-size:27px;line-height:34px;color:var(--navy)}
.guarantee{left:36px;top:308px;font-weight:700;font-size:35px;line-height:43px;color:var(--orange)}
.offer-band{left:0;top:411px;width:846px;height:45px;z-index:2;background:var(--sky);color:var(--white);
  font-family:"Questrial",sans-serif;font-size:26px;display:flex;align-items:center;justify-content:center}
.offer-band b{font-family:"Quicksand",sans-serif;font-weight:700;margin:0 7px}
.contact{left:36px;top:470px;width:392px;font-weight:600;font-size:20px;line-height:25.5px;color:var(--ink)}
.contact-row{display:flex;justify-content:space-between}
.section-title{font-weight:700;font-size:24px;color:var(--title)}
.panel{background:var(--panel)}
.feature-list{list-style:none}
.feature{position:relative;display:flex;align-items:center;font-weight:600;color:var(--navy)}
.icon{position:absolute;width:42px;height:42px;border-radius:50%;background:var(--white);border:3px solid var(--navy);
  display:flex;align-items:center;justify-content:center}
.icon svg{width:26px;height:26px}
.success .feature{height:52px;padding-left:60px;font-size:15.5px;line-height:19px}
.success .icon{left:-2px}
.subjects .feature{height:55px;padding-left:58px;font-size:15px;line-height:19px;flex-direction:column;align-items:flex-start;justify-content:center}
.subjects .icon{left:-12px;top:6px}
.subjects .light{font-family:"Questrial",sans-serif;font-weight:400;font-size:15px}
.subjects small{font-family:"Questrial",sans-serif;font-size:11px;line-height:12px}
.reasons{list-style:none;padding:6px 0 0 0}
.reason{display:flex;align-items:flex-start;font-weight:600;font-size:14.5px;line-height:17px;margin-bottom:8.4px}
.num{flex:none;width:21px;height:21px;border-radius:50%;border:1.5px solid var(--title);color:var(--navy);
  font-size:12px;display:flex;align-items:center;justify-content:center;margin:-2px 7px 0 -7px;background:var(--white)}
.map{left:618px;top:900px;width:136px;height:120px;background:#8fd0f0;border-radius:40% 30% 45% 35%}
.places{left:585px;top:1020px;width:210px;text-align:center;font-family:"Questrial",sans-serif;font-size:14px;line-height:17px;color:var(--ink)}
.cta-title{left:55px;top:1108px;font-weight:700;font-size:25px;color:var(--title)}
.cta-line{left:55px;font-weight:700;font-size:17px;color:var(--title)}
.cta-line span{color:var(--orange)}
.footer-brand{left:532px;top:1114px;display:flex;align-items:center;gap:10px}
.footer-brand .brand-dot{width:44px;height:44px}
.footer-brand .brand-name{font-size:25px}
.footer-tag{left:652px;top:1156px;font-weight:700;font-size:11px;color:var(--orange)}
</style>
</head>
<body>
<main class="flyer">
  <header>
    <div class="abs brand"><span class="brand-dot"></span><span class="brand-name">Brightpath Tutoring</span></div>
    <div class="abs tagline">Reach Your Potential!</div>
  </header>

  <div class="abs photo" role="img" aria-label="Child in a white shirt holding up a card stamped with an A* academic excellence seal, face hidden behind the card"></div>

  <p class="abs intro">Quality tuition by qualified &amp; experienced teachers, helping children ages 4-18 to realise their full potential!</p>
  <p class="abs guarantee">Money back<br>guaranteed results!</p>

  <div class="abs offer-band">Contact us today for a <b>Free Assessment</b> and <b>Free Trial!</b></div>

  <div class="abs contact">
    <div class="contact-row"><span>Phone:</span><span>0800 555 0192</span></div>
    <div class="contact-row"><span>Mobile:</span><span>07 700 900 318</span></div>
    <div class="contact-row"><span>Email:</span><span>info@brightpathtutoring.co.uk</span></div>
    <div class="contact-row"><span>Web:</span><span>brightpathtutoring.co.uk</span></div>
  </div>

  <section class="success">
    <h2 class="abs section-title" style="left:90px;top:610px">The Secret of Our Success</h2>
    <div class="abs panel" style="left:80px;top:639px;width:338px;height:207px"></div>
    <ul class="abs feature-list" style="left:48px;top:636px;width:360px">
      <li class="feature"><span class="icon"><svg viewBox="0 0 26 26"><path d="M7 6h5a2.5 2.5 0 1 1 4 0h4v5a2.5 2.5 0 1 1 0 4v5h-5a2.5 2.5 0 1 0-4 0H7z" fill="var(--sky)" transform="rotate(20 13 13)"/></svg></span>Personlalised Learning Plans to Suit Every Child</li>
      <li class="feature"><span class="icon"><svg viewBox="0 0 26 26" fill="none" stroke="var(--sky)" stroke-width="2.4" stroke-linecap="round"><path d="M13 24V13L6 5M13 13l7-8M13 17l6-3"/></svg></span>Different Students Require Different Approaches to Learning</li>
      <li class="feature"><span class="icon"><svg viewBox="0 0 26 26" fill="var(--sky)"><path d="M2 5h14v9H8l-4 3v-3H2z"/><path d="M10 12h14v9h-2v3l-4-3h-8z"/></svg></span>Working in Partership with Your Child's School</li>
      <li class="feature"><span class="icon"><svg viewBox="0 0 26 26" fill="none" stroke="var(--sky)" stroke-width="3" stroke-linecap="round" stroke-linejoin="round"><path d="M5 14l5 5L21 7"/></svg></span>Regular Tracking &amp; Feedback on Your Child's Progress</li>
    </ul>
  </section>

  <section class="subjects">
    <h2 class="abs section-title" style="left:491px;top:612px">Our Subjects</h2>
    <div class="abs panel" style="left:456px;top:639px;width:342px;height:208px"></div>
    <ul class="abs feature-list" style="left:456px;top:636px;width:340px">
      <li class="feature"><span class="icon"><svg viewBox="0 0 26 26" fill="var(--sky)"><rect x="9" y="2" width="8" height="8"/><rect x="4" y="12" width="8" height="8"/><rect x="14" y="12" width="8" height="8"/></svg></span>KS1, KS2 &amp; KS3<span class="light">English, Maths, Science</span></li>
      <li class="feature"><span class="icon"><svg viewBox="0 0 26 26" fill="var(--sky)"><rect x="3" y="6" width="4" height="15"/><rect x="9" y="4" width="4" height="17"/><rect x="15" y="7" width="4" height="14"/><rect x="2" y="22" width="22" height="2"/></svg></span>11+ &amp; Common Entrance Exam Preparation</li>
      <li class="feature"><span class="icon"><svg viewBox="0 0 26 26" fill="none" stroke="var(--sky)" stroke-width="2.2"><path d="M3 6c4-1 7 0 10 2 3-2 6-3 10-2v14c-4-1-7 0-10 2-3-2-6-3-10-2zM13 8v14"/></svg></span>GSCE<span class="light">English, Maths, Science</span><small>(call for further subjects)</small></li>
      <li class="feature"><span class="icon"><svg viewBox="0 0 26 26" fill="var(--sky)"><path d="M4 23L22 3c1 8-5 15-13 15z"/></svg></span>AS &amp; A2 Level<span class="light">English, Maths, Science</span><small>(call for further subjects)</small></li>
    </ul>
  </section>

  <section class="why">
    <h2 class="abs section-title" style="left:88px;top:858px">Why us? 7 great reasons</h2>
    <div class="abs panel" style="left:55px;top:885px;width:504px;height:207px"></div>
    <ol class="abs reasons" style="left:57px;top:887px;width:500px">
      <li class="reason"><span class="num">1</span>Qualified &amp; experienced tutors</li>
      <li class="reason"><span class="num">2</span>Individualised &amp; tailored learning plan to match your child's needs</li>
      <li class="reason"><span class="num">3</span>Communication link with your child's school for tracking &amp; feedback</li>
      <li class="reason"><span class="num">4</span>Weekly written reports issued on your child's progress</li>
      <li class="reason"><span class="num">5</span>Pupil progress guarantee</li>
      <li class="reason"><span class="num">6</span>Leadership Development training for character building and public speaking</li>
      <li class="reason"><span class="num">7</span>Confidence building and raising their aspirations</li>
    </ol>
  </section>

  <section class="locations">
    <h2 class="abs section-title" style="left:583px;top:860px">Locations covered</h2>
    <div class="abs panel" style="left:581px;top:885px;width:216px;height:207px"></div>
    <div class="abs map" role="img" aria-label="Map of the covered boroughs: Harrow, Hillingdon, Brent and Ealing"></div>
    <p class="abs places">Wembley - Harrow - Neasdon - Greenford - Southall &nbsp;Ealing Broadway - Hayes - Uxbridge - Kenton</p>
  </section>

  <footer>
    <h2 class="abs cta-title">Schedule a Tutoring Session today!</h2>
    <p class="abs cta-line" style="top:1136px">Call Now: <span>0800-555-0192</span> or</p>
    <p class="abs cta-line" style="top:1157px;color:var(--orange)">Book Online www.brightpathtutoring.co.uk</p>
    <div class="abs footer-brand"><span class="brand-dot"></span><span class="brand-name">Brightpath Tutoring</span></div>
    <div class="abs footer-tag">Reach Your Potential!</div>
  </footer>
</main>
</body>
</html>
```